Lose Up To 1 LB Of Fat Per Day

We need a double sided street sign for our weight loss clinic. We need the doctors picture to the right side of the sign and we need a challenge “Lose Up To 1 Pound Of Fat Per Day” included in the signage.
Our color scheme for the clinic are black, white, teal and silver.
The phone number should be at the bottom of the sign
517-294–6038

Target Market(s)

Weight Loss

Font styles to use
Sans Serif

```html
<!DOCTYPE html>
<html lang="en">
<head>
<meta charset="utf-8">
<title>Lose Up To 1 Pound Of Fat Per Day – Street Sign</title>
<link href="https://fonts.googleapis.com/css2?family=Montserrat:wght@300;400;500;700;800;900&display=swap" rel="stylesheet">
<style>
  :root {
    --black: #050607;
    --teal: #138278;
    --teal-deep: #0c5f5a;
    --white: #ffffff;
    --silver: #b9bec2;
    --silver-dark: #6f7579;
    --page: #e9ecee;
  }
  * { margin: 0; padding: 0; box-sizing: border-box; }
  html, body { width: 1200px; height: 1200px; overflow: hidden; }
  body {
    background: var(--page);
    font-family: "Montserrat", Arial, sans-serif;
    position: relative;
  }
  .sign {
    position: absolute;
    left: 0; top: 280px;
    width: 1200px; height: 640px;
    overflow: hidden;
    background:
      radial-gradient(ellipse 70% 90% at 88% 45%, var(--teal) 0%, var(--teal-deep) 38%, rgba(5,6,7,0) 75%),
      var(--black);
  }
  .brand {
    position: absolute;
    left: 44px; top: 40px;
    width: 150px;
    display: flex; flex-direction: column; align-items: center; gap: 10px;
    color: var(--white);
    font-weight: 500; font-size: 13px; letter-spacing: 1.5px;
    text-transform: uppercase; text-align: center; line-height: 1.3;
  }
  .brand-dot {
    width: 44px; height: 44px; border-radius: 50%;
    border: 2px solid var(--white);
  }
  .headline { position: absolute; left: 0; top: 0; width: 100%; height: 100%; }
  .headline span { position: absolute; line-height: 1; white-space: nowrap; }
  .hl-one {
    left: 250px; top: 44px;
    font-size: 265px; font-weight: 900; color: var(--teal);
    letter-spacing: -8px;
  }
  .hl-lose {
    left: 360px; top: 60px;
    font-size: 150px; font-weight: 900; color: var(--white);
    letter-spacing: -6px;
  }
  .hl-pound {
    left: 362px; top: 180px;
    font-size: 100px; font-weight: 900; color: var(--teal);
    letter-spacing: -3px;
  }
  .hl-offat {
    left: 530px; top: 262px;
    font-size: 46px; font-weight: 300; color: var(--teal);
    letter-spacing: 1px;
  }
  .hl-perday {
    left: 290px; top: 300px;
    font-size: 120px; font-weight: 800; color: var(--white);
    letter-spacing: -4px;
  }
  .divider {
    position: absolute; left: 0; top: 432px;
    width: 770px; height: 20px;
  }
  .phone {
    position: absolute; left: 60px; top: 470px;
    font-size: 96px; font-weight: 800; color: var(--white);
    letter-spacing: -1px; line-height: 1;
  }
  .doctor-photo {
    position: absolute; right: 30px; bottom: 0;
    width: 380px; height: 540px;
    border-radius: 190px 190px 0 0;
    background: linear-gradient(180deg, #2a3a3d 0%, #15191b 55%, #0b0d0e 100%);
  }
  .doctor-name {
    position: absolute; right: 40px; bottom: 34px;
    font-size: 15px; font-weight: 700; color: var(--white);
    letter-spacing: 1px; text-transform: uppercase;
  }
</style>
</head>
<body>
  <main class="sign">
    <div class="brand">
      <div class="brand-dot"></div>
      <div class="brand-name">Evergreen<br>Wellness<br>Clinic</div>
    </div>

    <h1 class="headline" aria-label="Lose 1 Pound of Fat Per Day">
      <span class="hl-one">1</span>
      <span class="hl-lose">Lose</span>
      <span class="hl-pound">Pound</span>
      <span class="hl-offat">OF FAT</span>
      <span class="hl-perday">Per Day</span>
    </h1>

    <svg class="divider" viewBox="0 0 770 20" aria-hidden="true">
      <defs>
        <linearGradient id="silverBar" x1="0" x2="1" y1="0" y2="0">
          <stop offset="0" stop-color="#6f7579"/>
          <stop offset="0.6" stop-color="#e3e6e8"/>
          <stop offset="1" stop-color="#9aa0a4"/>
        </linearGradient>
      </defs>
      <polygon points="0,4 760,12 760,18 0,10" fill="url(#silverBar)"/>
    </svg>

    <div class="phone">517-294–6038</div>

    <div class="doctor-photo" role="img" aria-label="Portrait photo of the clinic doctor in a dark suit and purple tie"></div>
    <div class="doctor-name">Dr. Martin Hale</div>
  </main>
</body>
</html>
```